Design business card for new business which advocates for elders in nursing homes or personal care h

New business for rights of the elderly residents who reside in personal care homes and or nursing homes. I am looking for a business card with logo of keystone for Pennsylvania and something in side the keystone that represents healthcare, advocates, something on that line; monitor care received and needs of resident. Chart audits, State Regulation compliance

Target Market(s)

Seniors no longer safe to live at home by themselves along with their kids

Industry/Entity Type

Business

Contact Information for Business Card

Keystone symbol to represent Pensylvaoa with some kind of symbol inside to represent advocate, seniors, or healthcare symbol

Font styles to use
Serif

Colors
33a6d7
85cae6
abd037

Requirements
Must have
• Brightwell Elder Allies is our business name; our tag line is Path to Better Living
Nice to have
• Nice logo

```html
<!DOCTYPE html>
<html lang="en">
<head>
<meta charset="utf-8">
<title>Brightwell Elder Allies – Business Card Options</title>
<link rel="stylesheet" href="https://fonts.googleapis.com/css2?family=Open+Sans:wght@400;600&family=Noto+Serif:wght@400&family=Arimo:wght@400&display=swap">
<style>
  :root {
    --blue: #33a6d7;
    --blue-light: #85cae6;
    --green: #abd037;
    --navy: #1f5f86;
    --grey: #6b7075;
    --ink: #222;
    --white: #fff;
    --card-border: #c9c9c9;
    --divider: #bdbdbd;
  }
  * { margin: 0; padding: 0; box-sizing: border-box; }
  html, body { width: 849px; height: 1200px; overflow: hidden; background: var(--white); }
  .sheet { position: relative; width: 849px; height: 1200px; }

  .option-label {
    position: absolute; left: 122px;
    font-family: "Arimo", sans-serif; font-size: 24px; color: var(--ink);
  }
  .divider { position: absolute; left: 0; top: 600px; width: 849px; height: 1px; background: var(--divider); }

  .card {
    position: absolute; left: 331px; width: 459px; height: 255px;
    border: 1px solid var(--card-border); background: var(--white); overflow: hidden;
  }
  .card svg.shape { position: absolute; left: 0; top: 0; width: 100%; height: 100%; }

  .sans { font-family: "Open Sans", sans-serif; }
  .serif { font-family: "Noto Serif", serif; }

  .brand { position: absolute; display: flex; align-items: center; }
  .brand-mark { background: var(--blue); flex: none; }
  .brand-name { color: var(--navy); font-weight: 400; white-space: nowrap; }
  .tagline { color: var(--grey); white-space: nowrap; }

  /* Option 1 – sans */
  .o1-front .brand { left: 95px; top: 48px; gap: 12px; }
  .o1-front .brand-mark { width: 40px; height: 40px; }
  .o1-front .brand-name { font-size: 24px; }
  .o1-front .tagline { position: absolute; left: 147px; top: 90px; font-size: 10px; letter-spacing: 5px; }

  .o1-back .brand { left: 18px; top: 18px; gap: 7px; }
  .o1-back .brand-mark { width: 22px; height: 22px; }
  .o1-back .brand-name { font-size: 14px; }
  .o1-back .tagline { position: absolute; left: 47px; top: 42px; font-size: 6.5px; letter-spacing: 3.2px; }

  .details { position: absolute; right: 20px; text-align: right; color: var(--white); white-space: nowrap; }
  .details .person { font-size: 20px; line-height: 1.1; }
  .details .role { font-size: 9px; margin-top: 3px; }
  .details.contact { font-size: 10px; line-height: 1.6; }
  .details.address { font-size: 9px; }

  .o1-back .person-block { top: 72px; }
  .o1-back .contact { top: 150px; }
  .o1-back .address { top: 222px; }

  /* Option 2 – serif */
  .o2-front .brand-mark { position: absolute; left: 207px; top: 22px; width: 44px; height: 44px; }
  .o2-front .brand-name { position: absolute; top: 78px; left: 0; width: 100%; text-align: center; font-size: 24px; }
  .o2-front .rule { position: absolute; left: 110px; top: 114px; width: 239px; height: 1px; background: var(--navy); }
  .o2-front .tagline { position: absolute; top: 120px; left: 0; width: 100%; text-align: center; font-size: 11px; letter-spacing: 6px; color: var(--navy); }

  .o2-back .brand-mark { position: absolute; left: 78px; top: 22px; width: 30px; height: 30px; }
  .o2-back .brand-name { position: absolute; left: 12px; top: 62px; font-size: 14px; }
  .o2-back .rule { position: absolute; left: 12px; top: 84px; width: 163px; height: 1px; background: var(--navy); }
  .o2-back .tagline { position: absolute; left: 12px; top: 88px; font-size: 7.5px; letter-spacing: 3.8px; color: var(--navy); }
  .o2-back .person-block { top: 60px; }
  .o2-back .contact { top: 134px; }
  .o2-back .address { top: 222px; }
</style>
</head>
<body>
<main class="sheet">

  <div class="option-label" style="top:284px;">Optin-1</div>

  <section class="card o1-front sans" style="top:28px;">
    <svg class="shape" viewBox="0 0 459 255" preserveAspectRatio="none" aria-hidden="true">
      <path d="M0 255 L0 200 C140 165 300 140 459 150 L459 255 Z" fill="var(--green)"/>
      <path d="M0 255 L0 196 C150 215 310 205 459 168 L459 255 Z" fill="var(--white)"/>
      <path d="M0 255 L0 202 C150 222 310 212 459 176 L459 255 Z" fill="var(--blue)"/>
    </svg>
    <div class="brand"><span class="brand-mark"></span><span class="brand-name">Brightwell Elder Allies</span></div>
    <div class="tagline">Path to Better Living</div>
  </section>

  <section class="card o1-back sans" style="top:306px;">
    <svg class="shape" viewBox="0 0 459 255" preserveAspectRatio="none" aria-hidden="true">
      <path d="M55 255 C130 140 250 40 459 18 L459 255 Z" fill="var(--green)"/>
      <path d="M67 255 C142 148 258 50 459 28 L459 255 Z" fill="var(--blue-light)"/>
      <path d="M78 255 C152 156 266 60 459 38 L459 255 Z" fill="var(--blue)"/>
    </svg>
    <div class="brand"><span class="brand-mark"></span><span class="brand-name">Brightwell Elder Allies</span></div>
    <div class="tagline">Path to Better Living</div>
    <div class="details person-block"><div class="person">Dana Whitford</div><div class="role">Advocate</div></div>
    <div class="details contact">Call: +1 555 014 2290<br>hello@brightwell.org<br>www.brightwell.org</div>
    <div class="details address">48 Orchard Ln, Lancaster PA</div>
  </section>

  <div class="divider"></div>

  <div class="option-label" style="top:898px;">Optin-2</div>

  <section class="card o2-front serif" style="top:645px;">
    <svg class="shape" viewBox="0 0 459 255" preserveAspectRatio="none" aria-hidden="true">
      <path d="M0 238 C150 232 330 200 459 128" fill="none" stroke="var(--blue-light)" stroke-width="3"/>
      <path d="M0 244 C150 238 330 208 459 140" fill="none" stroke="var(--green)" stroke-width="3"/>
      <path d="M0 255 L0 250 C160 246 330 218 459 152 L459 255 Z" fill="var(--blue)"/>
    </svg>
    <span class="brand-mark"></span>
    <div class="brand-name">Brightwell Elder Allies</div>
    <div class="rule"></div>
    <div class="tagline">Path to Better Living</div>
  </section>

  <section class="card o2-back serif" style="top:918px;">
    <svg class="shape" viewBox="0 0 459 255" preserveAspectRatio="none" aria-hidden="true">
      <path d="M230 0 C225 110 170 200 60 255" fill="none" stroke="var(--green)" stroke-width="3"/>
      <path d="M240 0 C235 112 182 204 78 255" fill="none" stroke="var(--blue-light)" stroke-width="3"/>
      <path d="M250 0 L459 0 L459 255 L95 255 C195 205 245 115 250 0 Z" fill="var(--blue)"/>
    </svg>
    <span class="brand-mark"></span>
    <div class="brand-name">Brightwell Elder Allies</div>
    <div class="rule"></div>
    <div class="tagline">Path to Better Living</div>
    <div class="details person-block"><div class="person">Dana Whitford</div><div class="role">Advocate</div></div>
    <div class="details contact">Call: +1 555 014 2290<br>hello@brightwell.org<br>www.brightwell.org</div>
    <div class="details address">48 Orchard Ln, Lancaster PA</div>
  </section>

</main>
</body>
</html>
```